Business card and stationery for VIP parking
Velmor Bay s.r.o.
I need double sided standard sized Business Card [3.5" x 2"]
Please, be creatives
Professional
Milan Vesecky
CEO
Na Lukách 512/27, Prague
Czech Republic 164 00
milan.vesecky@velmorbay.cz
www.velmorbay.cz
The business card should be very creative, professional, using the logo's color combinations. I also need envelopes, folders and all stationery set.
Some picture.

```html
<!DOCTYPE html>
<html lang="en">
<head>
<meta charset="utf-8">
<title>Velmor Bay – Business Card</title>
<link rel="stylesheet" href="https://fonts.googleapis.com/css2?family=Open+Sans:wght@400;600;700&display=swap">
<style>
  :root {
    --bg: #dfe1e4;
    --card-top: #ffffff;
    --card-bottom: #e9eaec;
    --brand-blue: #2b4c9b;
    --brand-red: #d0222b;
    --ink: #3a3d44;
    --muted: #8a8e96;
  }
  html, body {
    margin: 0;
    width: 1200px;
    height: 901px;
    overflow: hidden;
    background: var(--bg);
    font-family: "Open Sans", sans-serif;
  }
  .stage {
    position: relative;
    width: 1200px;
    height: 901px;
  }
  .card {
    position: absolute;
    top: 296px;
    width: 540px;
    height: 308px;
    border-radius: 22px;
    background: linear-gradient(160deg, var(--card-top) 0%, var(--card-bottom) 100%);
    box-shadow: 0 10px 26px rgba(0,0,0,0.18);
    overflow: hidden;
  }
  .card--back { left: 40px; }
  .card--front { left: 620px; }

  .brand {
    display: flex;
    align-items: center;
    gap: 10px;
  }
  .brand__mark {
    width: 30px;
    height: 30px;
    background: var(--brand-red);
  }
  .brand__name {
    font-weight: 700;
    font-size: 30px;
    color: var(--brand-blue);
    letter-spacing: -0.5px;
  }

  .back__brand {
    position: absolute;
    left: 0; right: 0;
    top: 118px;
    justify-content: center;
  }
  .back__url {
    position: absolute;
    left: 0; right: 0;
    top: 170px;
    text-align: center;
    font-size: 13px;
    letter-spacing: 2px;
    color: var(--muted);
  }

  .front__brand {
    position: absolute;
    left: 34px;
    top: 36px;
  }
  .front__address {
    position: absolute;
    left: 38px;
    top: 96px;
    font-size: 13px;
    line-height: 18px;
    color: var(--ink);
  }
  .front__contacts {
    position: absolute;
    left: 38px;
    top: 142px;
    margin: 0;
    padding: 0;
    list-style: none;
    font-size: 13px;
    line-height: 18px;
    color: var(--ink);
  }
  .front__contacts li {
    display: flex;
    align-items: center;
    gap: 8px;
  }
  .front__contacts svg { width: 12px; height: 12px; fill: var(--brand-blue); }
  .front__person {
    position: absolute;
    left: 318px;
    top: 176px;
  }
  .person__name {
    font-size: 15px;
    font-weight: 700;
    color: var(--brand-red);
  }
  .person__role {
    font-size: 12px;
    color: var(--ink);
  }
  .front__bands {
    position: absolute;
    left: 0;
    bottom: 0;
    width: 540px;
    height: 70px;
  }
  .front__url {
    position: absolute;
    left: 40px;
    bottom: 24px;
    font-size: 12px;
    letter-spacing: 2px;
    color: #ffffff;
  }
</style>
</head>
<body>
<main class="stage">
  <section class="card card--back" aria-label="Card back">
    <div class="brand back__brand">
      <span class="brand__mark"></span>
      <span class="brand__name">Velmor Bay</span>
    </div>
    <div class="back__url">www.velmorbay.cz</div>
  </section>

  <section class="card card--front" aria-label="Card front">
    <div class="brand front__brand">
      <span class="brand__mark"></span>
      <span class="brand__name">Velmor Bay</span>
    </div>
    <div class="front__address">
      Na Lukách 512/27, Prague<br>
      Czech Republic 164 00
    </div>
    <ul class="front__contacts">
      <li><svg viewBox="0 0 12 12"><path d="M2 1h3l1 3-1.5 1a6 6 0 0 0 2.5 2.5L8 6l3 1v3a1 1 0 0 1-1 1A9 9 0 0 1 1 2a1 1 0 0 1 1-1z"/></svg>+420 251 608 314</li>
      <li><svg viewBox="0 0 12 12"><rect x="3" y="0.5" width="6" height="11" rx="1.2"/></svg>+420 736 482 190</li>
      <li><svg viewBox="0 0 12 12"><path d="M0.5 2h11v8h-11z M1.5 3l4.5 3.5L10.5 3" fill="none" stroke="#2b4c9b" stroke-width="1.2"/></svg>milan.vesecky@velmorbay.cz</li>
    </ul>
    <div class="front__person">
      <div class="person__name">Milan Vesecky</div>
      <div class="person__role">CEO</div>
    </div>
    <svg class="front__bands" viewBox="0 0 540 70" aria-hidden="true">
      <polygon points="300,34 540,30 540,52 296,56" fill="var(--brand-red)"/>
      <polygon points="0,30 420,30 412,56 0,56" fill="var(--brand-blue)"/>
      <rect x="430" y="22" width="26" height="26" fill="var(--brand-red)" stroke="#ffffff" stroke-width="2"/>
    </svg>
    <div class="front__url">www.velmorbay.cz</div>
  </section>
</main>
</body>
</html>
```